Fired Up, Opt-in Focused,Wordpress Page: Bold Pulse

Here's the horrible page I just put up to share the info - BUT! it needs help majorly!!! www.boldpulse.me
I have a logo - you can work with it - or something new - this is a new site/business.
It's a fitness inspiration/makeover program.
I am part of the brand (see renaquist.com)
I can send more pics to work with.

Reason: Looking for a great site like:http://www.doratevenson.com/fit/

Target Market(s)

https://www.facebook.com/RenaQuistFitness - see my fans.

Industry/Entity Type

Fitness

Requirements
Must have
• Large opt-in box to my program at the top. Love Love Love http://www.hollybrandtner.com

Simple - easy to keep in wordpress. Not too much clutter. Easy design elements so I'm not dependant on a graphic designer for every graphic posting etc...

```html
<!DOCTYPE html>
<html lang="en">
<head>
<meta charset="utf-8">
<title>Bold Pulse – Fitness Motivation Made Easy</title>
<link rel="stylesheet" href="https://fonts.googleapis.com/css2?family=Source+Sans+3:wght@400;600;700;800&family=Arimo:wght@400;700&display=swap">
<style>
:root{
  --red:#d33b3e;
  --purple:#5b3a9e;
  --purple-text:#5f3fa2;
  --lilac:#ddd5ee;
  --frame:#d9d2ea;
  --footer:#41305f;
  --nav:#6b5c9a;
  --ink:#111;
  --body:#444;
  --white:#fff;
}
*{margin:0;padding:0;box-sizing:border-box}
html,body{width:1125px;height:1200px;overflow:hidden;background:var(--white)}
body{position:relative;font-family:"Source Sans 3",sans-serif;color:var(--ink)}
.abs{position:absolute}
.top-bar{left:0;top:0;width:1125px;height:8px;background:var(--red)}
.header{left:0;top:8px;width:1125px;height:77px;background:var(--white)}
.logo{left:202px;top:22px;display:flex;align-items:center;gap:8px;font-size:34px;font-weight:600;color:var(--nav);letter-spacing:-.5px}
.logo-dot{width:12px;height:12px;border-radius:50%;background:var(--red)}
.nav{right:209px;top:40px;display:flex;gap:27px;font-weight:700;font-size:14px;color:var(--nav)}
.nav .active{color:var(--ink)}
.hero-backdrop{left:0;top:85px;width:1125px;height:433px;background:linear-gradient(90deg,#4a3a36,#9a8a84 18%,#c9ccd2 82%,#5a6470)}
.hero-main{left:186px;top:85px;width:527px;height:433px;background:linear-gradient(120deg,#d9dce2 0%,#b58a78 35%,#8a5fb0 55%,#e08a3a 72%,#3a3a3a 100%)}
.hero-title{left:204px;top:385px;color:var(--white);font-weight:800;font-size:36px;line-height:45px;letter-spacing:-1.5px;text-shadow:0 1px 3px rgba(0,0,0,.4)}
.hero-dots{left:506px;top:496px;width:91px;height:22px;background:rgba(91,58,158,.85);display:flex;gap:7px;align-items:center;justify-content:center}
.hero-dots span{width:8px;height:8px;background:#eee}
.trainer{left:713px;top:85px;width:225px;height:433px;background:linear-gradient(180deg,#1a1414 0%,#6a4a3a 40%,#1b1b1b 85%,#2b8fb0 100%)}
.trainer-label{left:713px;top:473px;width:212px;text-align:right;color:#e6e6e6;font-weight:800;font-size:14px;line-height:18px;letter-spacing:-.6px}
.optin{left:186px;top:518px;width:750px;height:74px;background:var(--purple)}
.optin-title{left:207px;top:528px;color:var(--white);font-weight:800;font-size:24px;line-height:26px;letter-spacing:-.6px}
.field{top:538px;width:157px;height:29px;background:var(--white);border:1px solid #cfc8e0;font-size:11px;color:#999;padding:8px 11px}
.field.name{left:485px}.field.email{left:645px}
.signup{left:814px;top:538px;width:103px;height:28px;background:var(--red);border-radius:2px;color:var(--white);font-weight:700;font-size:11px;display:flex;align-items:center;justify-content:center;box-shadow:0 1px 2px rgba(0,0,0,.3)}
.promo{left:186px;top:604px;width:750px;height:216px;background:var(--lilac)}
.promo-photo{left:668px;top:604px;width:268px;height:216px;background:linear-gradient(100deg,rgba(221,213,238,0) 0%,#c49a86 35%,#5a3a30 75%,#2e2424 100%)}
.promo-title{left:206px;top:617px;font-weight:700;font-size:34px;letter-spacing:-1.3px}
.promo-sub{left:207px;top:659px;font-weight:700;font-size:20px;color:var(--purple-text);letter-spacing:-.5px}
.promo-text{left:207px;top:704px;width:370px;font-size:11.6px;line-height:14.6px;color:var(--body)}
.flex-icon{left:186px;top:766px;width:48px;height:54px;background:#8a84a0;border-radius:18px 22px 0 6px}
.card{top:838px;height:108px;border:5px solid var(--frame);background:var(--white)}
.card.events{left:186px;width:363px}
.card.about{left:590px;width:346px}
.card-title{font-weight:700;font-size:18px;letter-spacing:-.5px}
.events .card-title{left:14px;top:9px}
.event-lines{left:14px;top:44px;font-size:11.5px;line-height:12px;color:#555}
.link{color:var(--purple-text)}
.more{left:231px;top:49px;font-size:12px}
.about .card-title{left:16px;top:9px}
.about-text{left:18px;top:33px;width:190px;font-size:10px;line-height:11.3px;color:#555}
.about-text u{color:var(--purple-text)}
.about-photo{left:219px;top:1px;width:113px;height:78px;background:linear-gradient(135deg,#3a7a3a,#4a6ab0 50%,#1a1a1a)}
.footer-rule{left:186px;top:961px;width:750px;height:5px;background:var(--red)}
.footer{left:186px;top:968px;width:750px;height:232px;background:var(--footer);font-family:Arimo,sans-serif;color:var(--white)}
.footer h4{font-size:11.5px;font-weight:700;letter-spacing:.2px}
.quick{left:22px;top:16px;width:173px}
.quick ul{list-style:none;margin-top:10px}
.quick li{font-size:9px;border-bottom:1px solid #5a4a7a;padding:6px 0 5px 1px}
.tweets{left:240px;top:16px;width:240px}
.tweet{font-size:9px;line-height:11.5px;color:#ddd;margin-top:10px}
.tweet u{color:#ddd}
.connect{right:20px;top:12px;text-align:right}
.connect h4{font-size:11.5px}
.connect .sub{font-size:9px;color:#9a8fb0;margin:5px 0 8px}
.social{display:flex;justify-content:flex-end;align-items:center;gap:9px;font-size:9px;color:#ddd;height:21.5px}
.social i{width:17px;height:17px;border-radius:2px;display:block}
</style>
</head>
<body>
<div class="abs top-bar"></div>
<header class="abs header">
  <div class="abs logo"><span>boldpulse</span><span class="logo-dot"></span></div>
  <nav class="abs nav"><span>HOME</span><span>BLOG</span><span>CONNECT</span><span>FREE PERSONAL TRAINING</span><span class="active">MEET RENA</span></nav>
</header>

<div class="abs hero-backdrop" role="img" aria-label="Blurred gym interior"></div>
<div class="abs hero-main" role="img" aria-label="Smiling woman running on a treadmill in a group fitness class"></div>
<h1 class="abs hero-title">Fitness Motivation Made Easy.<br>&nbsp;Life Made Better.</h1>
<div class="abs hero-dots"><span></span><span></span><span></span><span></span><span></span></div>
<div class="abs trainer" role="img" aria-label="Personal trainer Rena standing with arms crossed"></div>
<div class="abs trainer-label">RENA<br>YOUR PERSONAL TRAINER</div>

<section class="abs optin"></section>
<h2 class="abs optin-title">Start your 7-Day Fitness<br>Makeover Now!</h2>
<div class="abs field name">Your Name</div>
<div class="abs field email">Your Email</div>
<div class="abs signup">SIGN UP</div>

<section class="abs promo"></section>
<div class="abs promo-photo" role="img" aria-label="Woman lifting a blue dumbbell"></div>
<h2 class="abs promo-title">Get Fit. Be Happy</h2>
<h3 class="abs promo-sub">Fitness Motivation Made Easy.&nbsp; Life Made Better</h3>
<p class="abs promo-text">The 7-Day "Bold Pulse Makeover" mini program will show you: 10 fitness mindsets that will set you for life The 2-step "get-off-the-couch process" you'll actually use The top 3 Fit For Life strategies ...and how to schedule it, do it, and always stay on track!</p>
<div class="abs flex-icon" role="img" aria-label="Flexed arm icon"></div>

<div class="abs card events">
  <div class="abs card-title">Torq90 &amp; Torq90 Plus</div>
  <div class="abs event-lines">Start Date: Mar. 3, 2013&nbsp; (FULL)<br>Start Date: April 1, 2013&nbsp; <span class="link">Join Now!</span></div>
  <div class="abs more link">Click for More Events</div>
</div>
<div class="abs card about">
  <div class="abs card-title">Meet RENA</div>
  <p class="abs about-text">I love being enthusiastic and motivating people to reach their potential, feel great and let go of limitations. Would love to connect with you! <u>Send a line and share your story…</u></p>
  <div class="abs about-photo" role="img" aria-label="Rena with her children"></div>
</div>

<div class="abs footer-rule"></div>
<footer class="abs footer">
  <div class="abs quick"><h4>QUICK LINKS</h4>
    <ul><li>HOME</li><li>ABOUT ME</li><li>FREE PERSONAL TRAINING</li><li>BLOG</li><li>CONNECT</li></ul>
  </div>
  <div class="abs tweets"><h4>LATEST TWEETS</h4>
    <p class="tweet">&nbsp;Here's my daily motivator to keep moving. StepTrack. My goal every day: 10,000 steps &lt;if it's 7pm and I've only hit...<br><u>bp.me/KR7n2aQ4 10 hours ago</u></p>
    <p class="tweet" style="margin-top:14px">Got my free t-shirt for sending in my Torq90 results in - rockin' it out today :) ***Actually Trimforge will send...<br><u>bp.me/Hs3Vt8Lp 2 days ago</u></p>
  </div>
  <div class="abs connect"><h4>Stay Connected</h4>
    <div class="sub">Follow us for the latest updates and deals</div>
    <div class="social">Like us on Circlebook <i style="background:#3b5998"></i></div>
    <div class="social">Watch us on Clipstream <i style="background:#c4302b"></i></div>
    <div class="social">Follow us on Chirper <i style="background:#4ab3e6"></i></div>
    <div class="social">View our Snapfolio photos <i style="background:#f2f2f2"></i></div>
  </div>
</footer>
</body>
</html>
```